2in1 Bartender & Sommelier needs a business card

I need a business card. I worked as a bartender in many places but I just finished a sommelier school and I would like a new business card. I like minimal design, natural materials and something what makes the people think :) I try to be creative in cocktail making, like little mixology, little twist on recipes... I like to travel and discover new places, cultures and of course interesting drinks and improve continously...live a little bit crazy life. And I like what I do...

Target Market(s)

restaurant/winebar managers, winemakers, other sommeliers and bartenders, people who work in food and beverage sector

Industry/Entity Type

Hospitality

Contact Information for Business Card

Rozsa Tarkany
Bartender & Sommelier
Phone: (FR) +33 6 4827 3190
(HU) +36 70 918 6352

Font styles to use
Script

Requirements
Must have
• Some sign, I am a bartender and sommelier as well.
Nice to have
• black and white maybe with 1 or 2 extra color
Should not have
• very colourful, to many things on the card

```html
<!DOCTYPE html>
<html lang="en">
<head>
<meta charset="utf-8">
<title>Rozsa Tarkany – Bartender &amp; Sommelier</title>
<link rel="stylesheet" href="https://fonts.googleapis.com/css2?family=Archivo:wght@800&family=Roboto+Condensed:wght@400&display=swap">
<style>
  :root {
    --stage: #ecebe8;
    --card: #ffffff;
    --ink: #111111;
    --ink-soft: #222222;
    --shadow: rgba(0, 0, 0, 0.28);
  }
  * { margin: 0; padding: 0; box-sizing: border-box; }
  html, body {
    width: 1200px;
    height: 1200px;
    overflow: hidden;
    background: var(--stage);
  }
  .stage {
    position: relative;
    width: 1200px;
    height: 1200px;
  }
  .card-holder {
    position: absolute;
    left: 100px;
    top: 300px;
    width: 1000px;
    height: 600px;
    filter: drop-shadow(0 14px 22px var(--shadow));
  }
  .card {
    position: relative;
    width: 1000px;
    height: 600px;
    background: var(--card);
    overflow: hidden;
    clip-path: path('M30,0 H970 Q1000,0 1000,30 V570 Q1000,600 970,600 H30 Q2,600 8,576 L120,300 L8,24 Q2,0 30,0 Z');
  }
  .identity {
    position: absolute;
    left: 150px;
    top: 70px;
  }
  .name {
    font-family: "Archivo", "Arial Black", sans-serif;
    font-weight: 800;
    font-size: 64px;
    letter-spacing: 1px;
    text-transform: uppercase;
    color: var(--ink);
    line-height: 1;
    white-space: nowrap;
  }
  .role {
    margin-top: 14px;
    font-family: "Roboto Condensed", "Arial Narrow", sans-serif;
    font-size: 34px;
    color: var(--ink-soft);
  }
  .contact {
    position: absolute;
    left: 150px;
    top: 250px;
    display: flex;
    gap: 22px;
    align-items: flex-start;
  }
  .phone-icon { width: 50px; height: 50px; flex: none; margin-top: 2px; }
  .phone-list {
    list-style: none;
    font-family: "Roboto Condensed", "Arial Narrow", sans-serif;
    font-size: 38px;
    line-height: 1.3;
    color: var(--ink);
    white-space: nowrap;
  }
</style>
</head>
<body>
<main class="stage">
  <div class="card-holder">
    <section class="card" aria-label="Business card">
      <div class="identity">
        <h1 class="name">Rozsa Tarkany</h1>
        <p class="role">Bartender &amp; Sommelier</p>
      </div>
      <div class="contact">
        <svg class="phone-icon" viewBox="0 0 50 50" aria-hidden="true">
          <rect x="0" y="0" width="50" height="50" rx="10" fill="#111"/>
          <path d="M11 21 Q25 10 39 21 L36 25 L31 23 L30 19 Q25 17 20 19 L19 23 L14 25 Z" fill="#fff"/>
          <path d="M17 26 L33 26 L37 38 L13 38 Z" fill="#fff"/>
          <circle cx="25" cy="31.5" r="3.5" fill="#111"/>
        </svg>
        <ul class="phone-list">
          <li>(FR) +33 6 4827 3190</li>
          <li>(HU) +36 70 918 6352</li>
        </ul>
      </div>
    </section>
  </div>
</main>
</body>
</html>
```